Food item ad for Brisk Falcon Restaurant

We need visual appealing poster for our restaurant food items, for 6 categories.
1. kebabs
-tandoori chicken tikka
- tandoori 1/2 chicken
-chicken seekh
- Chaplee chicken
- Multani lamb
- lamb bouti
- lamb chops
2. Meat lover gravy dishes
- Kadai chicken masala
- butter chicken boneless
- butter chicken
- Multani kofta curry
- lamb curry
- afghani haryali lamb
3. Try this @ Brisk falcon
- lamb Palou
- keema mantu
- meat thali
- kebob wraps
- chicken rolls
- sweet rice
- keema lasagna
- Romani roti
4. For vegetarian lovers
- 8 or 9 items pick n choose thali
- vegitarian
- vegitarian mantu
- aloo tikki cholay
- aloo tikki burger
- vada pav
- pav bhaji
- mix veg pakoras
5. Snakers
- sweet BBQ corn on the cob
- cassava fried
- cassava baked
- bhel puri
- sev puri
- chaat papri
- pain puri
6. Hot n cold
- Kashmiri tea. Mango milk shake
- Indian masala tea. Lessi
- English tea. Fresh juices
- green tea Fresh lime soda
- Indian style coffee Mint lime soda
We need six poster 1 for each category
it can be simple and similar theme in all six posters
the idea is to introduce the menu from my 2 Feet x 4 feet poster hanging from the window
facing the street
Updates
you go to the website:
pls take out 8-9 items in vegetarian lovers and also the word vegetarian
Industry/Entity Type
Restaurant
Requirements
Must have
- Brisk falcon chef logo attached
Some food graphics
- kebabs
- rice
- Romani roti
-Naan
Kitchen equipment graphics
- tandoor ( Indian clay oven )
-Grill
Fire, charcoal, spice ,lime etc
Brisk falcon color theme ,,,,,see attachments
food item names to give customer info about the menu

```html
<!DOCTYPE html>
<html lang="en">
<head>
<meta charset="utf-8">
<title>Brisk Falcon – Kababs</title>
<link rel="stylesheet" href="https://fonts.googleapis.com/css2?family=Jolly+Lodger&family=Mouse+Memoirs&display=swap">
<style>
  :root {
    --paper: #ffffff;
    --band: #effb9f;
    --ink: #1f1f1f;
    --heading-ink: #2b2b2b;
    --gold: #f2bb1c;
    --fire-hot: #ffd23a;
    --fire-mid: #f27a12;
    --fire-deep: #a81e0a;
    --grill-light: #e9c9a4;
    --grill-dark: #7a4a2a;
  }
  * { margin: 0; padding: 0; box-sizing: border-box; }
  html, body {
    width: 1200px; height: 2400px; overflow: hidden;
    background: var(--paper);
  }
  .poster {
    position: relative; width: 1200px; height: 2400px;
    background: var(--paper);
  }
  .brand {
    position: absolute; top: 0; left: 0; width: 1200px; height: 360px;
    display: flex; flex-direction: column; align-items: center; justify-content: center; gap: 18px;
  }
  .brand-dot {
    width: 170px; height: 170px; border-radius: 50%;
    background: var(--ink);
  }
  .brand-name {
    font-family: "Mouse Memoirs", sans-serif;
    font-size: 76px; line-height: 1; color: var(--gold);
    text-transform: uppercase; letter-spacing: 2px;
  }
  .category-title {
    position: absolute; top: 375px; left: 0; width: 1200px;
    text-align: center;
    font-family: "Jolly Lodger", cursive;
    font-size: 210px; line-height: 1; color: var(--heading-ink);
    letter-spacing: 4px;
  }
  .menu-band {
    position: absolute; top: 600px; left: 0; width: 1200px; height: 1076px;
    background: var(--band);
    display: flex; flex-direction: column; align-items: center; justify-content: center;
  }
  .menu-list { list-style: none; text-align: center; }
  .menu-item {
    font-family: "Mouse Memoirs", sans-serif;
    font-size: 118px; line-height: 146px; color: var(--ink);
  }
  .food-visual {
    position: absolute; top: 1700px; left: 0; width: 1200px; height: 360px;
    background: linear-gradient(90deg, var(--paper) 0%, var(--grill-light) 18%, var(--grill-dark) 55%, var(--grill-light) 85%, var(--paper) 100%);
  }
  .tagline {
    position: absolute; top: 2030px; left: 0; width: 1200px; height: 370px;
    display: flex; align-items: center; justify-content: center;
    font-family: "Jolly Lodger", cursive;
    font-size: 400px; line-height: 1; letter-spacing: 10px;
    color: var(--fire-mid);
    -webkit-text-stroke: 6px var(--ink);
    background: linear-gradient(180deg, var(--fire-hot), var(--fire-mid) 55%, var(--fire-deep));
    -webkit-background-clip: text; background-clip: text;
    -webkit-text-fill-color: transparent;
  }
</style>
</head>
<body>
  <main class="poster">
    <header class="brand">
      <span class="brand-dot"></span>
      <span class="brand-name">Brisk Falcon</span>
    </header>

    <h1 class="category-title">KABABS</h1>

    <section class="menu-band">
      <ul class="menu-list">
        <li class="menu-item">Tandoori Chicken Tikka</li>
        <li class="menu-item">Tandoori Half Chicken</li>
        <li class="menu-item">Chicken Seekh</li>
        <li class="menu-item">Chaplee Chicken</li>
        <li class="menu-item">Multani Lamb Bouti</li>
        <li class="menu-item">Lamb Chops</li>
      </ul>
    </section>

    <div class="food-visual" role="img" aria-label="Grilled chicken and vegetable kabab skewers"></div>

    <p class="tagline">SIZZLING</p>
  </main>
</body>
</html>
```